VARQO Business card

Black card, double sided with company colors black, blue and white with slogan on back Your VARQO......

Industry/Entity Type

Business

```html
<!DOCTYPE html>
<html lang="en">
<head>
<meta charset="utf-8">
<title>VARQO Business Card</title>
<link href="https://fonts.googleapis.com/css2?family=Roboto:wght@300;400;700;900&display=swap" rel="stylesheet">
<style>
  :root {
    --stage: #e6e4e0;
    --card-dark: #2a2b2d;
    --card-mid: #3d3e41;
    --brand-blue: #5ab8f0;
    --brand-blue-light: #7fcdfa;
    --text-white: #ffffff;
    --text-soft: #c9cbcf;
    --divider: #8a8c90;
  }
  * { box-sizing: border-box; margin: 0; padding: 0; }
  html, body { width: 1200px; height: 1000px; overflow: hidden; }
  body {
    background: var(--stage);
    font-family: "Roboto", Arial, sans-serif;
    position: relative;
  }
  .card {
    position: absolute;
    left: 250px;
    width: 700px;
    height: 400px;
    border-radius: 44px 0 44px 0;
    overflow: hidden;
    background: radial-gradient(ellipse at 35% 30%, var(--card-mid) 0%, var(--card-dark) 75%);
    box-shadow: 0 10px 30px rgba(0,0,0,0.25);
  }
  .card--back { top: 60px; }
  .card--front { top: 540px; }

  .brand {
    position: absolute;
    display: flex;
    align-items: center;
    gap: 14px;
  }
  .brand__dot {
    width: 26px; height: 26px;
    border-radius: 50%;
    background: var(--brand-blue);
  }
  .brand__name {
    font-weight: 700;
    font-size: 54px;
    letter-spacing: 3px;
    color: var(--text-white);
  }
  .card--back .brand { left: 210px; top: 220px; }
  .slogan {
    position: absolute;
    right: 50px; top: 60px;
    font-size: 15px;
    color: var(--text-white);
    font-weight: 400;
  }

  .card--front .brand { left: 60px; top: 130px; }
  .card--front .brand__name { font-size: 44px; }
  .divider {
    position: absolute;
    left: 330px; top: 60px;
    width: 1px; height: 200px;
    background: var(--divider);
  }
  .person { position: absolute; left: 360px; top: 52px; }
  .person__first {
    font-size: 42px; font-weight: 300; color: var(--text-white);
    line-height: 1; letter-spacing: 1px;
  }
  .person__last {
    font-size: 42px; font-weight: 900; color: var(--brand-blue);
    line-height: 1.05; letter-spacing: 1px;
  }
  .person__role { font-size: 13px; color: var(--text-soft); margin-top: 6px; }
  .contacts {
    list-style: none;
    margin-top: 18px;
    font-size: 12px;
    color: var(--text-soft);
  }
  .contacts li { display: flex; align-items: flex-start; gap: 10px; margin-bottom: 9px; line-height: 1.35; }
  .contacts svg { width: 12px; height: 12px; flex: none; margin-top: 2px; fill: var(--brand-blue); }
  .web-band {
    position: absolute;
    left: 0; right: 0; bottom: 0;
    height: 70px;
    background: linear-gradient(90deg, var(--brand-blue), var(--brand-blue-light));
    display: flex; align-items: center; justify-content: center;
    font-size: 22px; font-weight: 700; letter-spacing: 1px;
    color: var(--text-white);
  }
</style>
</head>
<body>

  <section class="card card--back" aria-label="Card back">
    <p class="slogan">The next generation of media broadcasting.</p>
    <div class="brand">
      <span class="brand__dot"></span>
      <span class="brand__name">VARQO</span>
    </div>
  </section>

  <section class="card card--front" aria-label="Card front">
    <div class="brand">
      <span class="brand__dot"></span>
      <span class="brand__name">VARQO</span>
    </div>
    <div class="divider"></div>
    <div class="person">
      <p class="person__first">LENA</p>
      <p class="person__last">MARSH</p>
      <p class="person__role">Founder &amp; CEO</p>
      <ul class="contacts">
        <li>
          <svg viewBox="0 0 12 12" aria-hidden="true"><path d="M6 0a4 4 0 0 0-4 4c0 3 4 8 4 8s4-5 4-8a4 4 0 0 0-4-4zm0 5.5A1.5 1.5 0 1 1 6 2.5a1.5 1.5 0 0 1 0 3z"/></svg>
          <span>418-76 Harbour Row<br>Calder Bay CB K2R 4M7</span>
        </li>
        <li>
          <svg viewBox="0 0 12 12" aria-hidden="true"><path d="M2.5 0.5l2 2.2-1 1.4c.7 1.5 1.9 2.7 3.4 3.4l1.4-1 2.2 2-1.2 2.2C5 10.5 1.5 7 .3 1.7z"/></svg>
          <span>1.800.555.0142</span>
        </li>
        <li>
          <svg viewBox="0 0 12 12" aria-hidden="true"><path d="M0 2h12v8H0zM1 3l5 3.5L11 3v-.2H1z"/></svg>
          <span>lena@varqomedia.com</span>
        </li>
      </ul>
    </div>
    <div class="web-band">www.varqomedia.com</div>
  </section>

</body>
</html>
```